Static landing page for our consulting business

Hi

I require a website for a company called "Koblane (Pty) Ltd"
It is a management consulting company with three core consulting services.
1. IT
2. Finance
3. Engineering

Our webpage basically needs a landing page with an overview and history of the company.

Then a sub section for each of the three disciplines with a description of what services are rendered. Each of these sections needs to have a link to the consultant that heads up that discipline.

Each consultant of which there are 3 potentially four shortly then needs a page that could introduce themselves, their qualifications etc.

There would also be a 'contact us & information page'
I have attached company logo for your reference.

Target Market(s)

Finance and management consulting

Industry/Entity Type

Business

Coding

Coded - Design and coding required

Number of Pages Required

1 page

Font styles to use
Sans Serif

Colors
33a6d7
85cae6
f68d4d
0492cd
f37122

Requirements
Must have
• basic html page with CSS, no back end or .net. Would run on a php server, and we would add the dynamic content ourselves if required later.
Nice to have
• Social media links, we would code them later.

```html
<!DOCTYPE html>
<html lang="en">
<head>
<meta charset="utf-8">
<title>Koblane (Pty) Ltd — Management Consulting</title>
<link href="https://fonts.googleapis.com/css2?family=Open+Sans:wght@400;600;700&display=swap" rel="stylesheet">
<style>
:root{
  --blue:#33a6d7;
  --blue-deep:#0492cd;
  --blue-light:#85cae6;
  --orange:#f37122;
  --orange-soft:#f68d4d;
  --ink:#333a40;
  --muted:#8a9299;
  --nav:#3a3f44;
  --footer:#163a5a;
  --footer-dark:#0f2b45;
  --white:#ffffff;
  --line:#e4e7ea;
}
*{box-sizing:border-box;margin:0;padding:0}
html,body{width:867px;height:1200px;overflow:hidden;background:var(--white)}
body{font-family:"Open Sans",Arial,sans-serif;color:var(--ink)}
a{color:inherit;text-decoration:none}

.site-header{height:95px;display:flex;align-items:center;padding:0 50px}
.brand{display:flex;align-items:center;gap:8px;font-size:22px;font-weight:700;color:var(--blue-deep)}
.brand-mark{width:22px;height:22px;border-radius:50%;background:var(--blue)}
.header-info{margin-left:auto;display:flex;align-items:center;gap:28px}
.info-item{display:flex;align-items:center;gap:6px;font-size:8px;line-height:1.35;color:var(--muted)}
.info-item strong{display:block;color:var(--ink);font-weight:600}
.btn{display:inline-block;font-size:8px;font-weight:700;letter-spacing:.5px;text-transform:uppercase;padding:8px 14px;border-radius:2px}
.btn-primary{background:var(--blue-deep);color:var(--white)}
.btn-outline{border:1px solid var(--white);color:var(--white)}

.main-nav{height:30px;background:var(--nav);display:flex;padding:0 50px}
.main-nav a{flex:1;text-align:center;line-height:30px;font-size:8px;font-weight:600;color:#d5d9dc;text-transform:uppercase}
.main-nav a.active{background:var(--blue);color:var(--white);flex:0 0 60px}

.hero{position:relative;height:335px}
.hero-photo{position:absolute;inset:0;background:linear-gradient(180deg,#c9d3dc 0%,#8e9eae 45%,#3d4a58 100%)}
.hero-shade{position:absolute;inset:0;background:linear-gradient(180deg,rgba(20,40,70,0) 40%,rgba(14,40,70,.55) 100%)}
.hero-copy{position:absolute;top:160px;left:0;right:0;text-align:center;color:var(--white)}
.hero-copy h1{font-size:24px;font-weight:700;letter-spacing:1px}
.hero-copy p{font-size:8.5px;line-height:1.5;margin:6px auto 16px;width:360px;color:#e6edf3}
.hero-copy .btn{margin:0 4px;padding:10px 20px}
.slider-arrow{position:absolute;top:170px;width:14px;height:26px;background:rgba(255,255,255,.35);display:flex;align-items:center;justify-content:center}
.slider-arrow.prev{left:12px}.slider-arrow.next{right:12px}

.services{padding:28px 50px 0;text-align:center}
.section-title{font-size:14px;font-weight:700;text-transform:uppercase;color:var(--ink)}
.section-lead{font-size:7px;color:var(--muted);margin:5px 0 22px;text-transform:uppercase;letter-spacing:.3px}
.service-cards{display:flex;gap:20px;justify-content:center}
.service-card{width:240px;border-bottom:1px solid var(--line);padding-bottom:12px}
.service-photo{height:115px;position:relative}
.service-photo.it{background:linear-gradient(160deg,#cfe4f1,#6fa2c6)}
.service-photo.finance{background:linear-gradient(160deg,#d8e7f1,#8aa8be)}
.service-photo.engineering{background:linear-gradient(160deg,#e9dfcf,#b0925f)}
.service-tab{position:absolute;right:0;top:35px;width:16px;height:44px;background:var(--blue-deep)}
.service-card h3{font-size:8px;font-weight:700;color:var(--blue);margin:14px 0 6px;text-transform:uppercase}
.service-card p{font-size:7px;line-height:1.5;color:var(--muted);padding:0 10px}
.read-more{display:inline-block;margin-top:8px;font-size:7px;color:var(--blue-deep);text-transform:uppercase;font-weight:600;border-bottom:1px solid var(--blue-light)}

.site-footer{position:absolute;top:830px;left:0;width:867px;height:370px;background:var(--footer)}
.footer-cols{display:flex;gap:60px;padding:28px 50px 0;color:#c7d3de}
.footer-cols h2{font-size:13px;font-weight:600;color:var(--white);margin-bottom:10px}
.about-col{flex:1.45}
.about-col p{font-size:7.5px;line-height:1.6;margin-bottom:9px}
.news-col{flex:1}
.news-item{display:flex;gap:10px;margin-bottom:12px;font-size:7.5px;line-height:1.55}
.news-date{flex:0 0 26px;height:26px;background:var(--white);color:var(--footer);text-align:center;font-size:7px;font-weight:700;line-height:1.2;padding-top:3px}
.news-date span{display:block;font-size:6px;font-weight:400}
.footer-bar{position:absolute;bottom:0;left:0;right:0;height:48px;background:var(--footer-dark);display:flex;align-items:center;padding:0 50px;font-size:7px;color:#9fb1c2}
.footer-links a{margin-right:10px}
.footer-bar .copy{display:block;margin-top:4px}
.footer-social{margin-left:auto;display:flex;align-items:center;gap:5px}
.social-dot{width:13px;height:13px;border-radius:50%}
.social-dot.a{background:var(--blue)}.social-dot.b{background:var(--blue-deep)}.social-dot.c{background:var(--orange)}.social-dot.d{background:var(--blue-light)}
</style>
</head>
<body>

<header class="site-header">
  <a class="brand" href="#"><span class="brand-mark"></span>Koblane (Pty) Ltd</a>
  <div class="header-info">
    <div class="info-item">
      <svg width="10" height="13" viewBox="0 0 10 13"><path d="M5 0a5 5 0 0 0-5 5c0 3.5 5 8 5 8s5-4.5 5-8a5 5 0 0 0-5-5zm0 7a2 2 0 1 1 0-4 2 2 0 0 1 0 4z" fill="#3a3f44"/></svg>
      <div><strong>1234 Company Name Street</strong>City, Province 0000</div>
    </div>
    <div class="info-item">
      <svg width="12" height="12" viewBox="0 0 12 12"><path d="M2.5 0.5l2 2.5-1.2 1.5a7 7 0 0 0 4.2 4.2L9 7.5l2.5 2-1.2 2C5 11.5 0.5 7 0.5 1.7z" fill="#3a3f44"/></svg>
      <div><strong>+011 555 0192</strong>Mon–Fri 8am–5pm</div>
    </div>
    <a class="btn btn-primary" href="#">Book a Consultant</a>
  </div>
</header>

<nav class="main-nav">
  <a class="active" href="#">Home</a>
  <a href="#">Our Services</a>
  <a href="#">About Us</a>
  <a href="#">Features</a>
  <a href="#">News</a>
  <a href="#">Contact Us</a>
</nav>

<section class="hero">
  <div class="hero-photo" role="img" aria-label="Team of business consultants standing together in an office"></div>
  <div class="hero-shade"></div>
  <a class="slider-arrow prev" href="#"><svg width="6" height="10" viewBox="0 0 6 10"><path d="M5 1L1 5l4 4" stroke="#fff" stroke-width="1.5" fill="none"/></svg></a>
  <a class="slider-arrow next" href="#"><svg width="6" height="10" viewBox="0 0 6 10"><path d="M1 1l4 4-4 4" stroke="#fff" stroke-width="1.5" fill="none"/></svg></a>
  <div class="hero-copy">
    <h1>NEQUE PORRO QUISQUAM</h1>
    <p>Expert management consulting across IT, finance and engineering. We help your business plan, grow and deliver results.</p>
    <a class="btn btn-primary" href="#">Get in Touch</a>
    <a class="btn btn-outline" href="#">Read More</a>
  </div>
</section>

<section class="services">
  <h2 class="section-title">Our Services</h2>
  <p class="section-lead">Three core disciplines led by experienced consultants who know your industry well</p>
  <div class="service-cards">
    <article class="service-card">
      <div class="service-photo it" role="img" aria-label="Modern office building against a blue sky"><span class="service-tab"></span></div>
      <h3>IT</h3>
      <p>Strategy, systems and infrastructure advice that keeps your technology aligned with your business goals.</p>
      <a class="read-more" href="#">Read more</a>
    </article>
    <article class="service-card">
      <div class="service-photo finance" role="img" aria-label="Business people shaking hands over a meeting table"><span class="service-tab"></span></div>
      <h3>Finance</h3>
      <p>Budgeting, reporting and financial planning support to help you make sound decisions with confidence.</p>
      <a class="read-more" href="#">Read more</a>
    </article>
    <article class="service-card">
      <div class="service-photo engineering" role="img" aria-label="Engineers in hard hats reviewing plans on site"><span class="service-tab"></span></div>
      <h3>Engineering</h3>
      <p>Project oversight, technical review and process design for engineering work of every size and scope.</p>
      <a class="read-more" href="#">Read more</a>
    </article>
  </div>
</section>

<footer class="site-footer">
  <div class="footer-cols">
    <div class="about-col">
      <h2>About Us</h2>
      <p>Koblane (Pty) Ltd is a management consulting firm founded to give growing businesses access to senior expertise.</p>
      <p>Over the years our team has advised clients across many sectors, building lasting partnerships based on trust, clear advice and measurable outcomes for every project we take on.</p>
      <p>Today our consultants lead three disciplines: IT, finance and engineering, each headed by a specialist with deep practical experience.</p>
    </div>
    <div class="news-col">
      <h2>Latest News</h2>
      <div class="news-item"><div class="news-date">12<span>MAR</span></div><p>New finance advisory service launched for small and medium businesses in the region.</p></div>
      <div class="news-item"><div class="news-date">04<span>FEB</span></div><p>Our engineering team completes a major infrastructure review for a long-standing client.</p></div>
      <div class="news-item"><div class="news-date">21<span>JAN</span></div><p>Welcoming a new senior consultant to strengthen our growing IT practice.</p></div>
    </div>
  </div>
  <div class="footer-bar">
    <div>
      <div class="footer-links"><a href="#">Home</a><a href="#">Our Services</a><a href="#">About Us</a><a href="#">Features</a><a href="#">News</a><a href="#">Contact Us</a></div>
      <span class="copy">Copyright © Koblane (Pty) Ltd. All Rights Reserved.</span>
    </div>
    <div class="footer-social">
      <span>Connect with us</span>
      <a class="social-dot a" href="#" aria-label="Social link"></a>
      <a class="social-dot b" href="#" aria-label="Social link"></a>
      <a class="social-dot c" href="#" aria-label="Social link"></a>
      <a class="social-dot d" href="#" aria-label="Social link"></a>
    </div>
  </div>
</footer>

</body>
</html>
```